Executive recruiting firm in need of business card design

Executive recruiting firm looking for a sleek, classy and modern business card design; card itself will be square shape, rounded edges and soft touch paper, our colors are dark blues in the navy color scale, silvers and grays. Reference our website for a better idea of our company's feel and goals at Staffvex.com - our company message is "Employee Engagement Begins at Recruitment" this should be on the card

Industry/Entity Type

Business

```html
<!DOCTYPE html>
<html lang="en">
<head>
<meta charset="utf-8">
<title>Staffvex Business Card</title>
<link href="https://fonts.googleapis.com/css2?family=Open+Sans:wght@400;700&display=swap" rel="stylesheet">
<style>
  :root {
    --navy: #1c1f6b;
    --navy-deep: #121450;
    --white: #ffffff;
    --gray-text: #5a5a66;
    --backdrop: #2b2b2e;
  }
  html, body {
    margin: 0;
    padding: 0;
    width: 1200px;
    height: 840px;
    overflow: hidden;
    background: var(--backdrop);
    font-family: "Open Sans", sans-serif;
  }
  .stage { position: relative; width: 1200px; height: 840px; }
  .card {
    position: absolute;
    width: 560px;
    height: 320px;
    border-radius: 6px;
    overflow: hidden;
    box-shadow: 0 10px 30px rgba(0,0,0,0.45);
  }
  .card-front {
    left: 90px; top: 90px;
    background: linear-gradient(135deg, var(--navy) 0%, var(--navy-deep) 100%);
    color: var(--white);
  }
  .card-back {
    left: 550px; top: 430px;
    background: var(--white);
    color: var(--navy);
  }
  .brand-name {
    position: absolute;
    margin: 0;
    font-weight: 700;
    font-size: 36px;
    letter-spacing: 2px;
    line-height: 1;
  }
  .card-front .brand-name {
    left: 0; right: 0; top: 112px;
    text-align: center;
    color: var(--white);
  }
  .slogan {
    position: absolute;
    left: 0; right: 0;
    top: 236px;
    margin: 0;
    text-align: center;
    font-size: 15px;
    font-weight: 400;
    color: var(--white);
  }
  .card-back .brand-name {
    left: 150px; top: 84px;
    color: var(--navy);
  }
  .rule { position: absolute; height: 2px; background: var(--navy); }
  .rule-right { left: 400px; right: 0; top: 102px; }
  .rule-left { left: 0; width: 150px; top: 176px; }
  .name-badge {
    position: absolute;
    left: 150px; top: 161px;
    width: 270px; height: 32px;
    border-radius: 16px;
    background: var(--navy);
    color: var(--white);
    font-size: 13px;
    font-weight: 700;
    display: flex; align-items: center; justify-content: center;
  }
  .name-badge .role { font-weight: 400; margin-left: 4px; }
  .address {
    position: absolute;
    right: 26px; top: 114px;
    text-align: right;
    font-size: 12.5px;
    line-height: 18px;
    color: var(--gray-text);
  }
  .contacts {
    position: absolute;
    left: 34px; top: 218px;
    list-style: none; margin: 0; padding: 0;
    font-size: 13px;
    line-height: 20px;
    color: var(--gray-text);
  }
  .contacts li { display: flex; align-items: center; gap: 8px; }
  .contacts svg { width: 12px; height: 12px; fill: var(--navy); }
</style>
</head>
<body>
<div class="stage">
  <section class="card card-front">
    <h1 class="brand-name">STAFFVEX</h1>
    <p class="slogan">Employee Engagement Begins at Recruitment</p>
  </section>

  <section class="card card-back">
    <h2 class="brand-name">STAFFVEX</h2>
    <div class="rule rule-right"></div>
    <div class="rule rule-left"></div>
    <div class="name-badge">DANIEL REYES -<span class="role">CEO/FOUNDER</span></div>
    <div class="address">
      240 Linden Ave<br>
      Larkspur, CA<br>
      www.staffvex.com
    </div>
    <ul class="contacts">
      <li><svg viewBox="0 0 12 12"><path d="M1 3c0-1 1-2 2-2h6c1 0 2 1 2 2v1H8V3H4v1H1z M2 5h8l1 6H1z"/></svg>555 214 7730</li>
      <li><svg viewBox="0 0 12 12"><path d="M3 0h6v12H3z M4 1v9h4V1z" fill-rule="evenodd"/></svg>555 390 1842</li>
      <li><svg viewBox="0 0 12 12"><path d="M3 0h6v4H3z M1 4h10v6H1z M3 10h6v2H3z"/></svg>555 726 4051</li>
      <li><svg viewBox="0 0 12 12"><path d="M0 2h12v8H0z M1 3l5 4 5-4z" fill-rule="evenodd"/></svg>daniel@staffvex.com</li>
    </ul>
  </section>
</div>
</body>
</html>
```